Bref créative
Quorel Stationary
Stationary and Business Cards
I need double sided standard sized Business Card [3.5" x 2"]
show me your ideas
Corporate
Marcus Toddin
Chief Executive Officer
Halvenor Business Tower
18th Floor
PO Box 58217
Dubai
United Arab Emirates
mt@quorel.co
www.quorel.co
Show me your ideas

```html
<!DOCTYPE html>
<html lang="en">
<head>
<meta charset="utf-8">
<title>Quorel Stationary – Corporate Identity Set</title>
<link rel="stylesheet" href="https://fonts.googleapis.com/css2?family=Open+Sans:wght@400;600&family=Libre+Baskerville:wght@400;700&display=swap">
<style>
  :root{
    --bg:#e7e4e0;
    --paper:#ffffff;
    --blue:#1aa3dc;
    --blue-deep:#0c86c4;
    --blue-light:#7fd0f2;
    --grey-swoosh:#d9dde1;
    --ink:#4a5560;
    --ink-soft:#8b96a0;
    --name-blue:#1c8fcf;
    --shadow:0 2px 6px rgba(0,0,0,.18);
  }
  *{box-sizing:border-box;margin:0;padding:0}
  html,body{width:1200px;height:915px;overflow:hidden;background:var(--bg)}
  body{position:relative;font-family:"Open Sans",Arial,sans-serif;color:var(--ink)}
  .piece{position:absolute;background:var(--paper);box-shadow:var(--shadow);overflow:hidden}
  .wave{position:absolute;left:0;bottom:0;width:100%;display:block;z-index:0}

  /* brand lockup: plain circle + name */
  .brand{display:flex;align-items:center;gap:6px;position:absolute;z-index:1}
  .brand-dot{border-radius:50%;background:var(--blue);flex:none}
  .brand-name{font-family:"Open Sans",Arial,sans-serif;font-weight:600;color:var(--blue);line-height:1}

  .small{font-size:7px;line-height:1.35;color:var(--ink-soft)}
  .white{color:#fff}
  address{font-style:normal}

  /* business cards */
  .card{width:176px;height:100px}
  .card-front{left:42px;top:48px}
  .card-front .brand{left:14px;top:22px}
  .card-front .holder{position:absolute;right:12px;top:14px;text-align:right;z-index:1}
  .card-front .holder-name{font-family:"Libre Baskerville",Georgia,serif;font-size:9px;color:var(--name-blue)}
  .card-back{left:214px;top:104px;background:linear-gradient(180deg,var(--blue-light),var(--blue) 55%,var(--blue-deep))}
  .card-back .brand{left:56px;top:32px}
  .card-back .brand-dot{background:#fff}
  .card-back .brand-name{color:#fff}
  .card-back .url{position:absolute;bottom:10px;width:100%;text-align:center}
  .card-plain{left:44px;top:196px}
  .card-plain .brand{left:20px;top:30px}
  .card-plain .url{position:absolute;bottom:10px;right:14px}

  /* envelope backs */
  .env-back{width:430px;height:170px}
  .env-back svg{position:absolute;inset:0;width:100%;height:100%}
  .env-back .brand{left:50%;transform:translateX(-50%)}
  .env-1{left:130px;top:300px}
  .env-1 .brand{top:14px}
  .env-2{left:78px;top:380px}
  .env-2 .brand{top:14px}
  .env-3{left:78px;top:460px}
  .env-3 .brand{top:16px}

  /* DL envelope front */
  .env-front{left:152px;top:566px;width:460px;height:190px}
  .env-front .brand{left:20px;top:22px}
  .env-front .address{position:absolute;left:24px;top:94px;z-index:1}

  /* letterhead */
  .letterhead{left:648px;top:168px;width:400px;height:560px}
  .letterhead .brand{left:28px;top:28px}
  .letterhead .watermark{position:absolute;left:112px;top:196px;display:flex;align-items:center;gap:14px;opacity:.12}
  .letterhead .watermark .brand-dot{width:120px;height:120px}
  .letterhead .watermark .brand-name{font-size:38px}
  .letterhead .footer-info{position:absolute;right:24px;bottom:122px;text-align:right;z-index:1}

  /* compliment slip */
  .comp{left:674px;top:742px;width:476px;height:138px}
  .comp .brand{left:22px;top:30px}
  .comp .divider{position:absolute;left:138px;top:22px;width:1px;height:74px;background:var(--grey-swoosh)}
  .comp .holder{position:absolute;left:156px;top:30px}
  .comp .holder-name{font-family:"Libre Baskerville",Georgia,serif;font-size:16px;color:var(--name-blue);font-weight:700}
  .comp .holder-role{font-family:"Libre Baskerville",Georgia,serif;font-size:9px;color:var(--ink);margin-top:3px}
  .comp .address{position:absolute;left:318px;top:28px}
  .comp .band{position:absolute;left:0;bottom:0;width:100%;height:20px;background:linear-gradient(90deg,var(--blue-deep),var(--blue),var(--blue-light));display:flex;align-items:center;justify-content:space-between;padding:0 18px}
</style>
</head>
<body>

<section class="piece card card-front" aria-label="Business card front">
  <div class="brand"><span class="brand-dot" style="width:24px;height:24px"></span><span class="brand-name" style="font-size:13px">quorel</span></div>
  <div class="holder">
    <p class="holder-name">Marcus Toddin</p>
    <p class="small">Chief Executive Officer</p>
  </div>
  <svg class="wave" viewBox="0 0 176 40" height="40" preserveAspectRatio="none" aria-hidden="true">
    <path d="M0 22 C50 8 110 36 176 14 L176 40 L0 40Z" fill="var(--grey-swoosh)"/>
    <path d="M0 28 C60 14 110 40 176 22 L176 40 L0 40Z" fill="var(--blue)"/>
  </svg>
</section>

<section class="piece card card-back" aria-label="Business card back">
  <div class="brand"><span class="brand-dot" style="width:22px;height:22px"></span><span class="brand-name" style="font-size:14px">quorel</span></div>
  <p class="url small white">www.quorel.co</p>
</section>

<section class="piece card card-plain" aria-label="Business card alternate">
  <div class="brand"><span class="brand-dot" style="width:26px;height:26px"></span><span class="brand-name" style="font-size:13px">quorel</span></div>
  <p class="url small">www.quorel.co</p>
</section>

<section class="piece env-back env-1" aria-label="Envelope back, grey flap">
  <svg viewBox="0 0 430 170" preserveAspectRatio="none" aria-hidden="true">
    <defs><linearGradient id="flapGrey" x1="0" y1="0" x2="0" y2="1"><stop offset="0" stop-color="#f2f3f4"/><stop offset="1" stop-color="#d4d8dc"/></linearGradient></defs>
    <polygon points="0,0 430,0 215,62" fill="url(#flapGrey)"/>
  </svg>
  <div class="brand"><span class="brand-dot" style="width:20px;height:20px"></span><span class="brand-name" style="font-size:11px">quorel</span></div>
</section>

<section class="piece env-back env-2" aria-label="Envelope back, blue flap">
  <svg viewBox="0 0 430 170" preserveAspectRatio="none" aria-hidden="true">
    <defs><linearGradient id="flapBlue" x1="0" y1="0" x2="0" y2="1"><stop offset="0" stop-color="var(--blue-light)"/><stop offset="1" stop-color="var(--blue)"/></linearGradient></defs>
    <polygon points="0,0 430,0 215,58" fill="url(#flapBlue)"/>
  </svg>
  <div class="brand"><span class="brand-dot" style="width:20px;height:20px;background:#fff"></span><span class="brand-name" style="font-size:11px;color:#fff">quorel</span></div>
</section>

<section class="piece env-back env-3" aria-label="Envelope back, white flap">
  <svg viewBox="0 0 430 170" preserveAspectRatio="none" aria-hidden="true">
    <polygon points="0,0 430,0 215,58" fill="#fafbfc" stroke="#d4d8dc" stroke-width="1"/>
  </svg>
  <div class="brand"><span class="brand-dot" style="width:20px;height:20px"></span><span class="brand-name" style="font-size:11px">quorel</span></div>
</section>

<section class="piece env-front" aria-label="Envelope front">
  <div class="brand"><span class="brand-dot" style="width:30px;height:30px"></span><span class="brand-name" style="font-size:16px">quorel</span></div>
  <address class="address small">
    Halvenor Business Tower<br>18th Floor<br>PO Box 58217<br>Dubai, United Arab Emirates
  </address>
  <svg class="wave" viewBox="0 0 460 70" height="70" preserveAspectRatio="none" aria-hidden="true">
    <defs><linearGradient id="waveBlue" x1="0" y1="0" x2="1" y2="0"><stop offset="0" stop-color="var(--blue-light)"/><stop offset=".5" stop-color="var(--blue)"/><stop offset="1" stop-color="var(--blue-deep)"/></linearGradient></defs>
    <path d="M0 30 C120 6 280 58 460 14 L460 70 L0 70Z" fill="var(--grey-swoosh)"/>
    <path d="M0 40 C140 16 290 66 460 26 L460 70 L0 70Z" fill="url(#waveBlue)"/>
  </svg>
</section>

<section class="piece letterhead" aria-label="Letterhead">
  <div class="brand"><span class="brand-dot" style="width:30px;height:30px"></span><span class="brand-name" style="font-size:16px">quorel</span></div>
  <div class="watermark" aria-hidden="true"><span class="brand-dot"></span><span class="brand-name">quorel</span></div>
  <address class="footer-info small">
    Halvenor Business Tower<br>18th Floor, PO Box 58217<br>Dubai, United Arab Emirates<br>www.quorel.co
  </address>
  <svg class="wave" viewBox="0 0 400 110" height="110" preserveAspectRatio="none" aria-hidden="true">
    <defs><linearGradient id="waveBlueLh" x1="0" y1="0" x2="1" y2="0"><stop offset="0" stop-color="var(--blue-light)"/><stop offset=".5" stop-color="var(--blue)"/><stop offset="1" stop-color="var(--blue-deep)"/></linearGradient></defs>
    <path d="M0 40 C110 10 250 70 400 18 L400 110 L0 110Z" fill="var(--grey-swoosh)"/>
    <path d="M0 52 C120 22 260 82 400 32 L400 110 L0 110Z" fill="url(#waveBlueLh)"/>
  </svg>
</section>

<section class="piece comp" aria-label="Compliment slip">
  <div class="brand"><span class="brand-dot" style="width:34px;height:34px"></span><span class="brand-name" style="font-size:15px">quorel</span></div>
  <span class="divider" aria-hidden="true"></span>
  <div class="holder">
    <p class="holder-name">Marcus Toddin</p>
    <p class="holder-role">Chief Executive Officer</p>
  </div>
  <address class="address small">
    Halvenor Business Tower<br>18th Floor<br>PO Box 58217<br>Dubai, United Arab Emirates<br>mt@quorel.co
  </address>
  <div class="band"><span class="small white">www.quorel.co</span><span class="small white">www.quorel.co</span></div>
</section>

</body>
</html>
```